Business Card Design

Looking for a clean professional Business card design with our logo. Needs to be able to customize name, address and contact info so we can use it multiple times with different people, please.

```html
<!DOCTYPE html>
<html lang="en">
<head>
<meta charset="utf-8">
<title>Brightpath Careers – Business Card</title>
<link rel="stylesheet" href="https://fonts.googleapis.com/css2?family=Roboto:wght@300;400;500;700&display=swap">
<style>
  :root {
    --brand-red: #c91f2e;
    --brand-red-dark: #a81824;
    --ink: #1f1f22;
    --ink-soft: #3a3a3f;
    --paper: #ffffff;
    --backdrop: #e6e7ea;
    --divider: #2a2a2e;
  }
  * { box-sizing: border-box; margin: 0; padding: 0; }
  html, body {
    width: 1200px; height: 900px; overflow: hidden;
    background: var(--backdrop);
    font-family: "Roboto", Arial, sans-serif;
    color: var(--ink);
  }
  .canvas { position: relative; width: 1200px; height: 900px; }

  .card {
    position: absolute;
    top: 296px;
    width: 540px; height: 308px;
    background: var(--paper);
    border-radius: 24px;
    overflow: hidden;
    box-shadow: 0 10px 28px rgba(0,0,0,0.12);
  }
  .card-front { left: 50px; }
  .card-back  { left: 610px; }

  /* Front */
  .name-band {
    position: absolute; left: 0; top: 0; right: 0; height: 118px;
    background: var(--brand-red);
    display: flex; align-items: center;
    padding-left: 34px;
  }
  .name-band .person-icon { width: 30px; height: 30px; fill: var(--ink); }
  .name-band .band-divider {
    width: 2px; height: 54px; background: var(--ink);
    margin: 0 22px 0 20px;
  }
  .holder-name {
    font-size: 28px; letter-spacing: 1px; color: var(--ink);
    font-weight: 300; text-transform: uppercase; line-height: 1.1;
  }
  .holder-name strong { font-weight: 700; }
  .holder-title { font-size: 14px; color: var(--ink-soft); margin-top: 4px; }

  .contact-block {
    position: absolute; left: 34px; top: 140px;
    display: flex;
  }
  .contact-icons {
    display: flex; flex-direction: column; gap: 18px;
    padding-top: 2px;
  }
  .contact-icons svg { width: 22px; height: 22px; fill: var(--ink); }
  .contact-divider {
    width: 2px; background: var(--divider);
    margin: 0 18px 0 18px;
  }
  .contact-lines { font-size: 13px; line-height: 19px; color: var(--ink); }

  .brand-lockup {
    position: absolute; right: 34px; bottom: 36px;
    display: flex; align-items: center; gap: 12px;
  }
  .brand-square { width: 40px; height: 40px; background: var(--brand-red); }
  .brand-name {
    font-size: 19px; font-weight: 500; color: var(--brand-red);
    text-transform: uppercase; line-height: 1.05; letter-spacing: 0.5px;
  }

  /* Back */
  .card-back .back-edge {
    position: absolute; left: 0; right: 0; bottom: 0; height: 14px;
    background: var(--brand-red);
  }
  .back-lockup {
    position: absolute; left: 0; right: 0; top: 100px;
    display: flex; justify-content: center; align-items: center; gap: 16px;
  }
  .back-lockup .brand-square { width: 58px; height: 58px; }
  .back-lockup .brand-name { font-size: 28px; }
  .back-website {
    position: absolute; left: 0; right: 0; top: 196px;
    text-align: center; font-size: 13px; color: var(--ink);
  }
</style>
</head>
<body>
<main class="canvas">

  <section class="card card-front" aria-label="Business card front">
    <div class="name-band">
      <svg class="person-icon" viewBox="0 0 24 24" aria-hidden="true">
        <rect x="0" y="0" width="24" height="24" rx="2" fill="none"/>
        <circle cx="12" cy="8" r="5"/>
        <path d="M2 23c0-5.5 4.5-9 10-9s10 3.5 10 9z"/>
      </svg>
      <span class="band-divider"></span>
      <div>
        <div class="holder-name">Jordan <strong>Reyes</strong></div>
        <div class="holder-title">General Manager</div>
      </div>
    </div>

    <div class="contact-block">
      <div class="contact-icons">
        <svg viewBox="0 0 24 24" aria-label="Address"><path d="M12 2 1 12h3v10h6v-6h4v6h6V12h3z"/></svg>
        <svg viewBox="0 0 24 24" aria-label="Phone"><path d="M6.6 10.8a15 15 0 0 0 6.6 6.6l2.2-2.2c.3-.3.7-.4 1-.2 1.1.4 2.3.6 3.6.6.6 0 1 .4 1 1V20c0 .6-.4 1-1 1A17 17 0 0 1 3 4c0-.6.4-1 1-1h3.5c.6 0 1 .4 1 1 0 1.3.2 2.5.6 3.6.1.3 0 .7-.2 1z"/></svg>
        <svg viewBox="0 0 24 24" aria-label="Web"><path d="M12 2a10 10 0 1 0 0 20 10 10 0 0 0 0-20zm6.9 6h-3a15 15 0 0 0-1.3-3.6A8 8 0 0 1 18.9 8zM12 4c.8 1.2 1.5 2.5 1.9 4h-3.8c.4-1.5 1.1-2.8 1.9-4zM4.3 14a8 8 0 0 1 0-4h3.4a16 16 0 0 0 0 4zm.8 2h3a15 15 0 0 0 1.3 3.6A8 8 0 0 1 5.1 16zm3-8h-3a8 8 0 0 1 4.3-3.6C8.8 5.5 8.4 6.7 8.1 8zM12 20c-.8-1.2-1.5-2.5-1.9-4h3.8c-.4 1.5-1.1 2.8-1.9 4zm2.3-6H9.7a14 14 0 0 1 0-4h4.6a14 14 0 0 1 0 4zm.3 5.6c.6-1.1 1-2.3 1.3-3.6h3a8 8 0 0 1-4.3 3.6zm1.7-5.6a16 16 0 0 0 0-4h3.4a8 8 0 0 1 0 4z"/></svg>
      </div>
      <span class="contact-divider"></span>
      <div class="contact-lines">
        <div>your address goes here</div>
        <div>42 Harbour Lane, Leeds</div>
        <div>+44 3100 4471 208</div>
        <div>+44 3100 4471 219</div>
        <div>jordan@brightpathcareers.com</div>
        <div>www.brightpathcareers.com</div>
      </div>
    </div>

    <div class="brand-lockup">
      <span class="brand-square"></span>
      <span class="brand-name">Brightpath<br>Careers</span>
    </div>
  </section>

  <section class="card card-back" aria-label="Business card back">
    <div class="back-lockup">
      <span class="brand-square"></span>
      <span class="brand-name">Brightpath<br>Careers</span>
    </div>
    <div class="back-website">www.brightpathcareers.com</div>
    <div class="back-edge"></div>
  </section>

</main>
</body>
</html>
```